Redesign of a growing event production company in atlanta!

www.qvrstaging.com - it's Plonko.com site and I'd like to keep it within PLONKO if possible.
We purchased a new logo and we are looking for a redesign.
We specialize in many different aspects of the event production industry and we want our page to be better segmented, with separation between the audio video lighting and wedding services offered.
We also want this cleaned up, showcasing client feedback and highlighted photos. Our industry is very visual and we want some of our work showcased as well as area for event videos.
We want the ability to add new photos and videos as well as links to our blog. If we can incorporate our blog into the site, that would be great as well.
Attached is the new logo, we are going to have it animated and placed on the site as well. We love the color spectrum of light and the significance to event production. We would like the page to incorporate that.

Target Market(s)

Women are the main purchasees of our services. brides between 20 - 40, and then corporate event planners...we have a high end market. We are marketing to the people who plan galas and society socials.

Industry/Entity Type

It Company

Number of Pages Required

5+ page

Font styles to use
Sans Serif
Script

Requirements
Must have
• incorporate the same content I currently have on my site.
• A clear but fluid separation between our event production services (Audio Visual) and the wedding services we offer. We MUST also be able to clearly show what we do. We are a one stop show and we want to convey that.
Nice to have
• Color palette based off logo attached

```html
<!DOCTYPE html>
<html lang="en">
<head>
<meta charset="utf-8">
<title>QVR Events</title>
<link rel="stylesheet" href="https://fonts.googleapis.com/css2?family=Open+Sans:ital,wght@0,400;0,600;0,700;1,400;1,600&display=swap">
<style>
:root{
  --black:#000;
  --plum:#76094c;
  --yellow:#d9cf12;
  --grey-band:#e5e5e5;
  --card:#eeeeee;
  --charcoal:#333;
  --text:#222;
  --muted:#444;
  --green:#5c8a2e;
  --teal:#2a6072;
  --blue:#1f6f9b;
  --olive:#6a8d2a;
  --white:#fff;
}
*{box-sizing:border-box;margin:0;padding:0}
html,body{width:1200px;height:2416px;overflow:hidden}
body{font-family:"Open Sans",Arial,sans-serif;color:var(--text);background:var(--white);position:relative}
.abs{position:absolute}
/* header */
.site-header{position:absolute;left:0;top:0;width:1200px;height:170px;background:var(--black)}
.brand{position:absolute;left:0;top:30px;width:1200px;display:flex;justify-content:center;align-items:center;gap:16px}
.brand-mark{width:80px;height:80px;border-radius:50%;border:3px solid #fff}
.brand-name{color:#fff;font-size:44px;font-weight:600;letter-spacing:1px}
.main-nav{position:absolute;left:151px;top:137px;width:898px;height:64px;background:var(--plum);display:flex;z-index:2}
.main-nav a{flex:1 1 auto;color:#fff;text-decoration:none;font-size:16px;white-space:nowrap;display:flex;align-items:center;justify-content:center;padding:0 16px;border-right:1px solid rgba(255,255,255,.15)}
.main-nav a:last-child{border-right:none}
/* hero */
.hero{position:absolute;left:0;top:170px;width:1200px;height:478px;overflow:hidden}
.hero-photo{position:absolute;inset:0;background:
  radial-gradient(ellipse at 50% 35%,rgba(240,220,180,.55),rgba(0,0,0,0) 55%),
  radial-gradient(ellipse at 35% 75%,rgba(255,255,255,.7),rgba(0,0,0,0) 22%),
  linear-gradient(180deg,#5b4a3a 0%,#3a2b22 45%,#2a1a14 75%,#3a1e12 100%)}
.hero-caption{position:absolute;left:0;bottom:0;width:1200px;height:92px;background:linear-gradient(180deg,rgba(0,0,0,0),rgba(0,0,0,.55))}
.hero-title{position:absolute;left:167px;top:416px;color:#fff;font-size:31px;letter-spacing:.5px;white-space:nowrap}
.btn-yellow{position:absolute;left:870px;top:428px;width:155px;height:40px;background:var(--yellow);border:2px solid #fff;border-radius:4px;color:#222;font-size:17px;display:flex;align-items:center;justify-content:center}
.slider-arrow{position:absolute;top:200px}
/* intro */
.intro{position:absolute;left:0;top:648px;width:1200px;height:308px;text-align:center}
.intro h1{position:absolute;left:0;top:42px;width:1200px;font-size:44px;font-weight:600;color:#111}
.intro .lead{position:absolute;left:250px;top:98px;width:700px;font-size:21px;line-height:26px;text-transform:uppercase;color:#111}
.intro .body{position:absolute;left:175px;top:162px;width:850px;font-size:14.5px;line-height:19px;color:var(--muted)}
/* services band */
.services-band{position:absolute;left:0;top:956px;width:1200px;height:463px;background:var(--grey-band)}
.service-card{position:absolute;top:63px;width:200px;height:280px;background:var(--card);text-align:center}
.service-card .strip{height:12px}
.service-card .photo{height:116px}
.service-card h3{font-size:18px;font-weight:400;margin-top:30px;color:#111;white-space:nowrap}
.service-card p{font-size:12.5px;line-height:15px;color:#333;padding:0 10px;margin-top:6px}
.service-btn{position:absolute;top:352px;width:200px;height:45px;color:#fff;font-size:15px;display:flex;align-items:center;justify-content:center;background:var(--charcoal)}
.service-btn.accent{background:var(--plum)}
/* blog/teach/services */
.info-row{position:absolute;left:0;top:1419px;width:1200px;height:399px}
.section-title{font-size:33px;font-weight:400;color:#111;text-transform:uppercase;line-height:36px;white-space:nowrap}
.blog-item{position:absolute;left:165px;width:210px;height:88px;border-bottom:1px solid #ccc}
.blog-thumb{position:absolute;left:0;top:4px;width:38px;height:38px;background:linear-gradient(135deg,#c8b8a6,#6d5a4a)}
.blog-text{position:absolute;left:46px;top:0;width:164px;font-size:13px;line-height:15.5px;color:#333}
.blog-text b{font-weight:700;color:#111}
.blog-text .date{display:block;color:var(--plum);font-style:italic;font-weight:700}
.teach-photo{position:absolute;left:411px;top:51px;width:108px;height:106px;background:linear-gradient(160deg,#6e4a3a,#2a1c16)}
.teach-title{position:absolute;left:527px;top:51px;font-size:29px;font-weight:400;line-height:38px;letter-spacing:-.2px;color:#111;text-transform:uppercase;white-space:nowrap}
.teach-by{position:absolute;left:527px;top:134px;font-size:19px;line-height:24px;color:#111;white-space:nowrap}
.teach-by span{color:var(--plum)}
.teach-copy{position:absolute;left:411px;width:420px;font-size:13px;line-height:17px;color:#333}
.service-list{position:absolute;left:831px;top:97px;list-style:none}
.service-list li{height:28.7px;display:flex;align-items:center;gap:10px;font-size:13px;font-weight:700;color:#111;white-space:nowrap}
.service-list li.active{color:var(--olive)}
/* events */
.events-band{position:absolute;left:0;top:1818px;width:1200px;height:320px;background:var(--grey-band)}
.event{position:absolute;top:104px;width:265px}
.event .cal{position:absolute;left:0;top:0}
.event h4{position:absolute;left:60px;top:0;font-size:19px;font-weight:700;color:#111;white-space:nowrap}
.event .month{position:absolute;left:60px;top:28px;font-size:12px;color:#222}
.event p{position:absolute;left:0;top:54px;width:265px;font-size:13px;line-height:15.5px;font-style:italic;color:#222}
.event .btn{position:absolute;left:0;top:115px;width:117px;height:36px;background:var(--charcoal);color:#fff;font-size:15px;display:flex;align-items:center;justify-content:center}
.event .btn.accent{background:var(--plum)}
/* footer */
.site-footer{position:absolute;left:0;top:2138px;width:1200px;height:231px}
.footer-col{position:absolute;top:36px}
.footer-col h5{font-size:19px;font-weight:400;text-transform:uppercase;color:#111;margin-bottom:8px}
.footer-col ul{list-style:none}
.footer-col li{font-size:12px;line-height:20px;text-transform:uppercase;color:#222;display:flex;align-items:center;gap:8px}
.sq{width:13px;height:13px;background:#2b4a7a;display:inline-block}
.contact li{text-transform:none;align-items:flex-start;line-height:16px;margin-bottom:12px}
.legal{position:absolute;left:0;top:2369px;width:1200px;height:47px;background:var(--black);color:#ccc;font-size:12px;display:flex;align-items:center;justify-content:center}
.legal b{color:#fff}
</style>
</head>
<body>

<header class="site-header">
  <div class="brand">
    <span class="brand-mark"></span>
    <span class="brand-name">QVR EVENTS</span>
  </div>
</header>
<nav class="main-nav">
  <a>GET INSPIRED</a><a>SERVICES OFFERED</a><a>QVR OWNERS</a><a>CLIENT REFERRALS</a><a>BLOG</a><a>CONTACT US</a>
</nav>

<section class="hero">
  <div class="hero-photo" role="img" aria-label="Bride and groom dancing in a grand ballroom surrounded by guests"></div>
  <div class="hero-caption"></div>
  <svg class="slider-arrow" style="left:95px" width="42" height="42" viewBox="0 0 42 42"><circle cx="21" cy="21" r="20" fill="rgba(255,255,255,.35)"/><path d="M24 12 L15 21 L24 30" stroke="#fff" stroke-width="3" fill="none"/></svg>
  <svg class="slider-arrow" style="left:1063px" width="42" height="42" viewBox="0 0 42 42"><circle cx="21" cy="21" r="20" fill="rgba(255,255,255,.35)"/><path d="M18 12 L27 21 L18 30" stroke="#fff" stroke-width="3" fill="none"/></svg>
  <div class="hero-title">ENTRUST US WITH YOUR EVENT</div>
  <div class="btn-yellow">READ MORE</div>
</section>

<section class="intro">
  <h1>Hello There!</h1>
  <p class="lead">Liquam rhoncus, libero non congue ultri nterdum velit congue ultri nterdqu am sed nisi.</p>
  <p class="body">Mes cuml dia sed in lacus ut eniascet etor ingerto aliiqt es sitet amet eismod ictorut dolore ligulate ameti dapi licdu nt mtsent lusto dolor ltisim comme. Mes cuml dia sed inertio lacus ut eniascet ingerto aliiqt sit eism odictor. Ut ligulate ameti dapibus ticdu mtsent dolorltiis sim. Mes cuml dia sed in lacus ut enia etor. ingerto dolore ipsum commete mtsent aliiqt. Es sitet amet eismod ictor ut ligulate ameti dapibusti mtsent lusto dolor ltisim comme.</p>
</section>

<section class="services-band">
  <article class="service-card" style="left:171px">
    <div class="strip" style="background:var(--green)"></div>
    <div class="photo" role="img" aria-label="Birthday party guests around a cake with candles" style="background:linear-gradient(135deg,#b7642e,#e0b04a 50%,#6b3a1e)"></div>
    <h3>Birthday Parties</h3>
    <p>Dolor nunc vule putateulr ips dol consem donec semp ertet laciniate ultricie upien disse comete dolo lectus fgilla.</p>
  </article>
  <article class="service-card" style="left:389px">
    <div class="strip" style="background:var(--plum)"></div>
    <div class="photo" role="img" aria-label="Wedding couple in a church aisle" style="background:linear-gradient(135deg,#3a3a3a,#d8d6d2 55%,#555)"></div>
    <h3>Wedding Planning</h3>
    <p>Dolor nunc vule putateulr ips dol consem donec semp ertet laciniate ultricie upien disse comete dolo lectus fgilla.</p>
  </article>
  <article class="service-card" style="left:608px">
    <div class="strip" style="background:var(--teal)"></div>
    <div class="photo" role="img" aria-label="Corporate event guests mingling with drinks" style="background:linear-gradient(135deg,#2b2b33,#8a8478 55%,#3b3a3e)"></div>
    <h3>Corporate Events</h3>
    <p>Dolor nunc vule putateulr ips dol consem donec semp ertet laciniate ultricie upien disse comete dolo lectus fgilla.</p>
  </article>
  <article class="service-card" style="left:825px">
    <div class="strip" style="background:var(--blue)"></div>
    <div class="photo" role="img" aria-label="Audio video mixing desk in front of a lit stage screen" style="background:linear-gradient(180deg,#2b3550,#7a5a3a 55%,#1c1c22)"></div>
    <h3>Audio Video Lighting</h3>
    <p>Dolor nunc vule putateulr ips dol consem donec semp ertet laciniate ultricie upien disse comete dolo lectus fgilla.</p>
  </article>
  <div class="service-btn" style="left:171px">READ MORE</div>
  <div class="service-btn accent" style="left:389px">READ MORE</div>
  <div class="service-btn" style="left:608px">READ MORE</div>
  <div class="service-btn" style="left:825px">READ MORE</div>
</section>

<section class="info-row">
  <h2 class="section-title abs" style="left:165px;top:50px">Our Blog</h2>
  <div class="blog-item" style="top:100px">
    <div class="blog-thumb" role="img" aria-label="Blog author portrait"></div>
    <p class="blog-text"><b>Dolor nunc vulputateulr</b> ips dol consec. Dodfhdnec semp efhrtet lacin iate. <span class="date">- 31 March, 2015</span></p>
  </div>
  <div class="blog-item" style="top:190px">
    <div class="blog-thumb" role="img" aria-label="Blog author portrait"></div>
    <p class="blog-text"><b>Dolor nunc vulputateulr</b> ips dol consec. Dodfhdnec semp efhrtet lacin iate. <span class="date">- 25 March, 2015</span></p>
  </div>
  <div class="blog-item" style="top:280px;border-bottom:none">
    <div class="blog-thumb" role="img" aria-label="Blog author portrait"></div>
    <p class="blog-text"><b>Dolor nunc vulputateulr</b> ips dol consec. Dodfhdnec semp efhrtet lacin iate. <span class="date">- 12 March, 2015</span></p>
  </div>

  <div class="teach-photo" role="img" aria-label="Portrait of the company manager"></div>
  <h2 class="teach-title">We will teach you<br>how to celebrate</h2>
  <p class="teach-by">- Mara Lentz : <span>Manager</span></p>
  <p class="teach-copy" style="top:182px">Dolor nunc vule putateulr ips dol consec. Donec semp efhrtet lacn iate ultricie upien disse comete dolo lectus fgilla itollicil tua ffludin dolor nec met quam accumsan. Dolore condime netus lullam ipsu utlacus adipiscing ipsum molestie euismod lore.</p>
  <p class="teach-copy" style="top:277px">Vule putateulr ips dol consec.Donec semp efhrtet lacindfiate ultriicie upien disse comete dolo lectus fgilla itollicil tua luddffin dolor nec met quam accumsan. Dolore condime netus lullafhm ipsu utlacus adipiscing ipsum molestie euismod lore.</p>

  <h2 class="section-title abs" style="left:831px;top:50px">Our Services</h2>
  <ul class="service-list">
    <li><svg width="10" height="14"><path d="M2 1 L8 7 L2 13" stroke="#555" stroke-width="2" fill="none"/></svg>LOREM IPSUM DOLOR SIAM</li>
    <li class="active"><svg width="10" height="14"><path d="M2 1 L8 7 L2 13" stroke="#555" stroke-width="2" fill="none"/></svg>LOREM IPSUM DOLOR SIAM</li>
    <li><svg width="10" height="14"><path d="M2 1 L8 7 L2 13" stroke="#555" stroke-width="2" fill="none"/></svg>LOREM IPSUM DOLOR SIAM</li>
    <li><svg width="10" height="14"><path d="M2 1 L8 7 L2 13" stroke="#555" stroke-width="2" fill="none"/></svg>LOREM IPSUM DOLOR SIAM</li>
    <li><svg width="10" height="14"><path d="M2 1 L8 7 L2 13" stroke="#555" stroke-width="2" fill="none"/></svg>LOREM IPSUM DOLOR SIAM</li>
    <li><svg width="10" height="14"><path d="M2 1 L8 7 L2 13" stroke="#555" stroke-width="2" fill="none"/></svg>LOREM IPSUM DOLOR SIAM</li>
    <li><svg width="10" height="14"><path d="M2 1 L8 7 L2 13" stroke="#555" stroke-width="2" fill="none"/></svg>LOREM IPSUM DOLOR SIAM</li>
    <li><svg width="10" height="14"><path d="M2 1 L8 7 L2 13" stroke="#555" stroke-width="2" fill="none"/></svg>LOREM IPSUM DOLOR SIAM</li>
    <li><svg width="10" height="14"><path d="M2 1 L8 7 L2 13" stroke="#555" stroke-width="2" fill="none"/></svg>LOREM IPSUM DOLOR SIAM</li>
  </ul>
</section>

<section class="events-band">
  <h2 class="section-title abs" style="left:165px;top:50px">Upcoming Events</h2>
  <svg class="abs" style="left:967px;top:54px" width="62" height="30" viewBox="0 0 62 30">
    <circle cx="15" cy="15" r="12" fill="none" stroke="#aaa" stroke-width="2"/><path d="M18 9 L12 15 L18 21" stroke="#aaa" stroke-width="2.5" fill="none"/>
    <circle cx="47" cy="15" r="12" fill="none" stroke="#555" stroke-width="2"/><path d="M44 9 L50 15 L44 21" stroke="#555" stroke-width="2.5" fill="none"/>
  </svg>
  <div class="event" style="left:165px">
    <svg class="cal" width="48" height="48" viewBox="0 0 48 48"><rect x="2" y="6" width="44" height="40" rx="3" fill="#fff" stroke="var(--plum)" stroke-width="3"/><rect x="2" y="6" width="44" height="10" fill="var(--plum)"/><rect x="11" y="1" width="4" height="10" fill="var(--plum)"/><rect x="33" y="1" width="4" height="10" fill="var(--plum)"/><text x="24" y="39" text-anchor="middle" font-family="Open Sans,sans-serif" font-size="19" fill="#111">31</text></svg>
    <h4>DOLOR NUNC VULEPU</h4><span class="month">MARCH, 2015</span>
    <p>Aliquam dapibus tincidunt metus. Praesent justo dolor, lobortis quis, lobortis dignissim, pulvinar ac, lorem.</p>
    <div class="btn accent">READ MORE</div>
  </div>
  <div class="event" style="left:469px">
    <svg class="cal" width="48" height="48" viewBox="0 0 48 48"><rect x="2" y="6" width="44" height="40" rx="3" fill="#fff" stroke="var(--plum)" stroke-width="3"/><rect x="2" y="6" width="44" height="10" fill="var(--plum)"/><rect x="11" y="1" width="4" height="10" fill="var(--plum)"/><rect x="33" y="1" width="4" height="10" fill="var(--plum)"/><text x="24" y="39" text-anchor="middle" font-family="Open Sans,sans-serif" font-size="19" fill="#111">20</text></svg>
    <h4>DOLOR NUNC VULEPU</h4><span class="month">MARCH, 2015</span>
    <p>Aliquam dapibus tincidunt metus. Praesent justo dolor, lobortis quis, lobortis dignissim, pulvinar ac, lorem.</p>
    <div class="btn">READ MORE</div>
  </div>
  <div class="event" style="left:773px">
    <svg class="cal" width="48" height="48" viewBox="0 0 48 48"><rect x="2" y="6" width="44" height="40" rx="3" fill="#fff" stroke="var(--plum)" stroke-width="3"/><rect x="2" y="6" width="44" height="10" fill="var(--plum)"/><rect x="11" y="1" width="4" height="10" fill="var(--plum)"/><rect x="33" y="1" width="4" height="10" fill="var(--plum)"/><text x="24" y="39" text-anchor="middle" font-family="Open Sans,sans-serif" font-size="19" fill="#111">12</text></svg>
    <h4>DOLOR NUNC VULEPU</h4><span class="month">MARCH, 2015</span>
    <p>Aliquam dapibus tincidunt metus. Praesent justo dolor, lobortis quis, lobortis dignissim, pulvinar ac, lorem.</p>
    <div class="btn">READ MORE</div>
  </div>
</section>

<footer class="site-footer">
  <div class="footer-col" style="left:165px">
    <h5>Navigations</h5>
    <ul><li>Get Inspired</li><li>Services Offered</li><li>QVR Owners</li><li>Client Referrals</li><li>Blog</li><li>Contact Us</li></ul>
  </div>
  <div class="footer-col" style="left:389px">
    <h5>For Members</h5>
    <ul><li>Forums</li><li>Promotions</li><li>Sign In</li><li>News</li></ul>
  </div>
  <div class="footer-col" style="left:614px">
    <h5>Follow Us</h5>
    <ul><li><span class="sq"></span>Friendspace</li><li><span class="sq"></span>Cliptube</li><li><span class="sq"></span>Worklink</li><li><span class="sq"></span>Travel Notes</li><li><span class="sq"></span>Filmreel</li><li><span class="sq"></span>Photogram</li></ul>
  </div>
  <div class="footer-col contact" style="left:821px">
    <h5>Our Location</h5>
    <ul>
      <li><svg width="12" height="16" viewBox="0 0 12 16"><path d="M6 0 C2.7 0 0 2.6 0 5.8 C0 10 6 16 6 16 C6 16 12 10 12 5.8 C12 2.6 9.3 0 6 0Z" fill="#555"/><circle cx="6" cy="6" r="2.2" fill="#fff"/></svg><span>Sed ut perspiciatis unde omnis iste<br>error sit voluptatem</span></li>
      <li><svg width="14" height="14" viewBox="0 0 14 14"><path d="M3 1 L5 4 L4 6 C5 8 6 9 8 10 L10 9 L13 11 L12 13 C6 13 1 8 1 2Z" fill="#555"/></svg><span>555-014-2280</span></li>
      <li><svg width="14" height="14" viewBox="0 0 14 14"><rect x="3" y="0" width="8" height="14" rx="1.5" fill="#555"/><rect x="4.5" y="2" width="5" height="8" fill="#fff"/></svg><span>(555) 013-7741</span></li>
      <li><svg width="14" height="12" viewBox="0 0 14 12"><rect x="0" y="1" width="14" height="10" fill="#555"/><path d="M0 1 L7 7 L14 1" stroke="#fff" stroke-width="1.2" fill="none"/></svg><span>support@qvrstaging.com</span></li>
    </ul>
  </div>
</footer>
<div class="legal">©&nbsp;2015&nbsp;<b>QVR Events</b>, LLC. All Rights Reserved.</div>

</body>
</html>
```